Business Card Design Project

I need some business cards with the logo you did for us (attached)
I am looking for a coulourful yet serious business card

We do market research
on the back I want the logo

on the front my name : Corinne Valdessac
position : Manager
address : Brume Analytica Sarl - 27 Rue des tanneurs
1847 Glarency - Switzerland
corinne.valdessac@brumeanalytica.ch
Tel : +4122 934 07 58
Mob France :+33 671 42 8356
Mob Italy +39 347 520 8163

The tree of the logo could also be used alone

THE BACKGROUND COLOR ON THE FRONT HAS TO BE WHITE, ON THE BACK YU CAN TRY OHER COLOUR BUT HOMOGENEOUS (NOT EXPENSIVE TO PRINT)

Target Market(s)

multinational companies or other market research companies

Industry/Entity Type

Market Research

Requirements
Must have
• logo on the back
and all the info above

```html
<!DOCTYPE html>
<html lang="en">
<head>
<meta charset="utf-8">
<title>Brume Analytica – Business Cards</title>
<link rel="stylesheet" href="https://fonts.googleapis.com/css2?family=Quicksand:wght@300;400;500&display=swap">
<style>
  :root {
    --backdrop: #e4e4e4;
    --card: #ffffff;
    --brand-pink: #d6245f;
    --text-grey: #8a8a8a;
  }
  * { margin: 0; padding: 0; box-sizing: border-box; }
  html, body {
    width: 1157px;
    height: 1200px;
    overflow: hidden;
    background: var(--backdrop);
    font-family: "Quicksand", sans-serif;
  }
  .canvas { position: relative; width: 1157px; height: 1200px; }

  .card {
    position: absolute;
    left: 237px;
    width: 686px;
    height: 400px;
    background: var(--card);
  }
  .card--logo {
    top: 145px;
    display: flex;
    align-items: center;
    justify-content: center;
  }
  .card--contact { top: 616px; }

  /* Logo side: wordmark centred in the card */
  .brand-lockup {
    display: flex;
    align-items: center;
    gap: 22px;
    margin-top: -8px;
  }
  .brand-dot {
    width: 34px; height: 34px;
    border-radius: 50%;
    background: var(--brand-pink);
  }
  .brand-name {
    font-weight: 500;
    font-size: 66px;
    line-height: 1;
    color: var(--brand-pink);
    letter-spacing: -0.5px;
  }

  /* Contact side */
  .contact-mark {
    position: absolute;
    left: 276px; top: 24px;
    width: 130px; height: 130px;
    border-radius: 50%;
    background: var(--brand-pink);
  }
  .person {
    position: absolute;
    left: 0; right: 0;
    text-align: center;
    font-weight: 300;
    color: var(--text-grey);
    font-size: 18px;
    line-height: 24px;
  }
  .person__name-line { top: 161px; }
  .person__name { color: var(--brand-pink); font-weight: 400; }
  .person__email { top: 188px; }

  .address, .phones {
    position: absolute;
    font-weight: 300;
    font-size: 18px;
    line-height: 27.5px;
    color: var(--text-grey);
  }
  .address { left: 35px; top: 258px; font-style: normal; }
  .phones { right: 38px; top: 284px; text-align: right; }
  .phones .number { color: var(--brand-pink); font-weight: 400; }
</style>
</head>
<body>
<main class="canvas">
  <section class="card card--logo" aria-label="Logo side">
    <div class="brand-lockup">
      <span class="brand-dot"></span>
      <span class="brand-name">brume analytica</span>
    </div>
  </section>

  <section class="card card--contact" aria-label="Contact side">
    <div class="contact-mark"></div>
    <p class="person person__name-line"><span class="person__name">Corinne Valdessac</span> _ Manager</p>
    <p class="person person__email">corinne.valdessac@brumeanalytica.ch</p>

    <address class="address">
      Brume Analytica Sarl,<br>
      27 Rue des Tanneurs<br>
      1847 Glarency,<br>
      Switzerland
    </address>

    <div class="phones">
      Tel.: <span class="number">+4122 934 07 58</span><br>
      Mob. France: <span class="number">+33 671 42 8356</span><br>
      Mob. Italy: <span class="number">+39 347 520 8163</span>
    </div>
  </section>
</main>
</body>
</html>
```